Nanny Share Ecommerce Website for Finding Childcare and Parents who need Childcare HuggaSitter.com

Our company needs an ecommerce website (HuggaSitter.com) for a US subscription based service strictly for nanny sharing that connects families and caregivers. The website would allow families to connect with one another as well as to search for nannies. The service would be searchable for other families by location (by radius or zip code), children demographic (age range/gender/special needs), days of week or times, after school care, school closure days (holidays), etc. The service would also be searchable for nannies based on gender, provider age range, years experience, language, hourly rate, transportation available, certification (CPR first aid), education etc. The search fields would be searchable and sortable and allow to connect with the provider (after paying subscription fee). The service would be similar to tendly.com in that it would allow for families and caregivers to post photos as well as a short bio of the themselves. There would also be a feedback/star rating mechanism to rate caregivers who have performed work for families (viewable to public). The service would be free for nannies to post their bios and only a subscription based service for families to connect with other families or with caregivers (able to view bio but need service to connect). There will be a short bio on the benefits of nanny sharing (reduced cost, increased flexibility for parents, reduced illness, increased socialization with other children vs. sole nanny), as well as Q&A section with best practices.

Target Market(s)

Families, Nannies

Industry/Entity Type

Childcare

Logo Text

Hugga Sitter

Coding

Coded - Design and coding required

Number of Pages Required

5+ page

Requirements
Must have
• Searchable (need to be able to search for families as well as nannies), responsive, functional, easy to use, add value to families and nannies. Needs to be able to collect payment for subscription.
Nice to have
• Optimized for mobile, SEO optimized

```html
<!DOCTYPE html>
<html lang="en">
<head>
<meta charset="utf-8">
<title>Hugga Sitter – Nanny Sharing</title>
<link rel="stylesheet" href="https://fonts.googleapis.com/css2?family=Quicksand:wght@400;500;600;700&display=swap">
<style>
:root{
  --navy:#2a2d6d;
  --navy-deep:#22255e;
  --pink:#f7b6c8;
  --pink-light:#fbd3de;
  --pink-text:#f48bae;
  --ink:#4a4a5a;
  --muted:#7a7a88;
  --white:#ffffff;
}
*{box-sizing:border-box;margin:0;padding:0}
html,body{width:1200px;height:3607px;overflow:hidden}
body{position:relative;background:var(--white);font-family:"Quicksand",sans-serif;color:var(--ink)}
.abs{position:absolute}
.btn{position:absolute;background:var(--navy);color:var(--white);font-size:11px;font-weight:700;display:flex;align-items:center;justify-content:center;border-radius:2px;white-space:nowrap}
.center{text-align:center;left:0;width:1200px}

/* hero */
.hero-photo{left:0;top:0;width:1200px;height:577px;background:linear-gradient(100deg,#6a6f8e 0%,#a7aec0 35%,#e8dcd6 60%,#f1e6e2 80%,#eef0f3 100%)}
.hero-fade{left:0;top:400px;width:1200px;height:177px;background:linear-gradient(180deg,rgba(255,255,255,0),#fff)}
.header{left:168px;top:24px;width:862px;height:60px;background:var(--white);box-shadow:0 2px 8px rgba(0,0,0,.12);white-space:nowrap}
.header > *{position:absolute;top:50%;transform:translateY(-50%)}
.logo{left:20px;font-size:20px;font-weight:700;color:var(--navy);display:flex;align-items:center;gap:8px}
.logo-dot{width:14px;height:14px;border-radius:50%;background:var(--pink-text)}
.nav{left:279px;display:flex;gap:20px;font-size:11px;font-weight:600;color:var(--navy)}
.nav .active{border-bottom:2px solid var(--navy);padding-bottom:3px}
.phone{left:584px;font-size:12px;font-weight:700;color:var(--navy);display:flex;align-items:center;gap:6px}
.socials{left:745px;display:flex;gap:10px}
.socials span{width:14px;height:14px;border-radius:50%;background:#c9cad8}
.socials span.on{background:var(--navy)}
.hero-title{left:200px;top:170px;width:250px;text-align:center;color:var(--white);font-size:28px;font-weight:700}
.hero-sub{left:200px;top:204px;width:250px;text-align:center;color:var(--white);font-size:22px;font-weight:500}
.search{left:221px;top:240px;width:207px;height:36px;background:var(--white);border-radius:3px;font-size:10px;color:var(--muted);padding:12px 8px}
.adv{left:352px;top:295px;color:var(--white);font-size:11px;font-weight:700;white-space:nowrap}
.thumb{position:absolute;top:409px;width:164px;height:104px;border-radius:4px;border:3px solid var(--white)}
.thumb-label{position:absolute;top:518px;font-size:11px;font-weight:600;color:var(--navy);white-space:nowrap}
.arrow{position:absolute;top:446px;width:28px;height:28px;border-radius:50%;display:flex;align-items:center;justify-content:center}

/* welcome */
.eyebrow{font-size:15px;font-weight:700;color:var(--navy)}
.heading-pink{font-size:30px;font-weight:700;color:var(--pink-text)}
.para{font-size:12px;line-height:17px;color:var(--muted)}

/* date night */
.date-photo{left:0;top:842px;width:1200px;height:200px;background:linear-gradient(90deg,#3b5a2a,#6d8c3c 35%,#a3b35a 60%,#8aa34a 80%,#4b6d33)}

/* how it works */
.step-circle{position:absolute;top:1162px;width:182px;height:182px;border-radius:50%;background:var(--white);display:flex;align-items:center;justify-content:center}
.step-title{position:absolute;top:1350px;width:220px;text-align:center;font-size:14px;font-weight:700;color:var(--navy)}
.step-text{position:absolute;top:1378px;width:220px;text-align:center;font-size:11px;line-height:16px;color:#6a5a68}

/* testimonials */
.quote{position:absolute;top:1717px;width:338px;height:116px;background:var(--pink-light);border-radius:6px;padding:18px 32px;font-size:13px;line-height:19px;font-weight:700;color:var(--navy)}
.quote::after{content:"";position:absolute;left:46px;bottom:-12px;border:12px solid transparent;border-top-color:var(--pink-light);border-bottom:0}
.avatar{position:absolute;top:1856px;width:40px;height:40px;border-radius:50%;background:linear-gradient(135deg,#c9a18d,#6d5a55)}
.who{position:absolute;top:1860px;font-size:13px;font-weight:700;color:var(--navy);white-space:nowrap}
.who small{display:block;font-size:10px;font-weight:500;color:var(--muted);margin-top:3px}

/* demographic */
.demo-photo{left:260px;top:2166px;width:318px;height:318px;border-radius:50%;border:6px solid var(--white);background:linear-gradient(135deg,#f2ece6,#d8cbc3 55%,#8d93b3)}
.demo-text{left:613px;top:2182px;width:350px;font-size:14px;line-height:21px;font-weight:700;color:var(--white)}
.bullet{position:absolute;left:616px;font-size:11px;color:#d9dbef;display:flex;align-items:center;gap:12px;white-space:nowrap}
.bullet i{width:10px;height:10px;border-radius:50%;border:2px solid var(--pink)}

/* blog */
.ghost{position:absolute;top:2708px;font-size:40px;font-weight:700;color:#f3f3f6}
.post-img{position:absolute;top:2742px;width:262px;height:144px;border-radius:3px;box-shadow:0 4px 10px rgba(0,0,0,.15)}
.post-title{position:absolute;top:2900px;font-size:14px;font-weight:600;color:var(--pink-text)}
.post-meta{position:absolute;top:2922px;font-size:9px;color:var(--muted);white-space:nowrap}
.post-text{position:absolute;top:2944px;width:250px;font-size:11px;line-height:16px;color:var(--muted)}

/* footer */
.footer{left:0;top:3283px;width:1200px;height:324px;background:var(--navy)}
.f-col{position:absolute;top:3330px;width:220px;text-align:center;color:var(--white)}
.f-icon{width:44px;height:44px;margin:0 auto 12px;display:flex;align-items:center;justify-content:center}
.f-col h4{font-size:14px;font-weight:700;margin-bottom:6px}
.f-col p{font-size:10px;line-height:14px;color:#d6d8ee}
.f-rule{left:248px;top:3482px;width:704px;height:1px;background:rgba(255,255,255,.2)}
.f-logo{left:248px;top:3530px;font-size:30px;font-weight:700;color:var(--white);white-space:nowrap}
.f-social{left:512px;top:3540px;display:flex;gap:14px}
.f-social span{width:16px;height:16px;border-radius:50%;background:#9ea1c9}
.f-social span.on{background:var(--pink)}
.f-copy{left:700px;top:3543px;font-size:10px;color:#d6d8ee;white-space:nowrap}
</style>
</head>
<body>

<!-- Hero -->
<div class="abs hero-photo" role="img" aria-label="Mother and young daughter smiling together at home"></div>
<div class="abs hero-fade"></div>

<header class="abs header">
  <div class="logo"><span class="logo-dot"></span>Hugga Sitter</div>
  <nav class="nav">
    <span class="active">Home</span><span>About</span><span>Features</span><span>Our Blog</span><span>Contact Us</span>
  </nav>
  <div class="phone">
    <svg width="12" height="12" viewBox="0 0 24 24"><path fill="#f48bae" d="M6.6 10.8a15 15 0 0 0 6.6 6.6l2.2-2.2c.3-.3.7-.4 1-.2 1.1.4 2.3.6 3.6.6.6 0 1 .4 1 1V20c0 .6-.4 1-1 1A17 17 0 0 1 3 4c0-.6.4-1 1-1h3.5c.6 0 1 .4 1 1 0 1.3.2 2.5.6 3.6.1.3 0 .7-.2 1z"/></svg>
    0 (555) 014-2270
  </div>
  <div class="socials"><span></span><span></span><span></span><span class="on"></span><span></span></div>
</header>

<h1 class="abs hero-title">Nanny Near You</h1>
<div class="abs hero-sub">by radius or zip code</div>
<div class="abs search">E.g. Boston</div>
<div class="btn" style="left:221px;top:290px;width:84px;height:26px">Search</div>
<div class="abs adv">Advance Search</div>

<div class="thumb" style="left:173px;background:linear-gradient(135deg,#e6d3c4,#c29a84)" role="img" aria-label="Mother and child photo"></div>
<div class="thumb" style="left:346px;background:linear-gradient(135deg,#4d3f44,#b98d8a)" role="img" aria-label="Mother hugging daughter photo"></div>
<div class="thumb" style="left:519px;background:linear-gradient(135deg,#e6dc8d,#c8a06b)" role="img" aria-label="Family outdoors photo"></div>
<div class="thumb" style="left:693px;background:linear-gradient(135deg,#8d6d55,#e3c9a5);border-color:var(--navy)" role="img" aria-label="Mother and child photo"></div>
<div class="thumb-label" style="left:185px">Lorem Ipsum</div>
<div class="thumb-label" style="left:358px">Simply Dummy</div>
<div class="thumb-label" style="left:531px">Lorem Ipsum</div>
<div class="thumb-label" style="left:705px">Simply Dummy</div>
<div class="arrow" style="left:972px;background:#fff"><svg width="10" height="10" viewBox="0 0 10 10"><path d="M6.5 1.5 3 5l3.5 3.5" stroke="#2a2d6d" stroke-width="1.8" fill="none"/></svg></div>
<div class="arrow" style="left:1003px;background:var(--navy)"><svg width="10" height="10" viewBox="0 0 10 10"><path d="M3.5 1.5 7 5 3.5 8.5" stroke="#fff" stroke-width="1.8" fill="none"/></svg></div>

<!-- Welcome -->
<div class="abs center eyebrow" style="top:600px">Welcome to</div>
<h2 class="abs center heading-pink" style="top:620px">Hugga Sitter</h2>
<p class="abs para" style="left:326px;top:670px;width:548px;text-align:center">Lorem Ipsum is simply dummy text of the printing and typesetting industry. Lorem Ipsum has been the industry's standard dummy text ever since the 1500s, when an unknown printer took a galley of type and scrambled it to make a type specimen book. It has survived not only five centuries, but also the leap into electronic typesetting, remaining essentially unchanged.</p>
<div class="btn" style="left:556px;top:764px;width:88px;height:27px">Nanny More</div>

<!-- Date night -->
<div class="abs date-photo" role="img" aria-label="Mother kissing her little daughter in a sunny garden"></div>
<div class="abs center" style="top:890px;font-size:22px;font-weight:700;color:#fff">Need a Date Night?</div>
<div class="abs center" style="top:920px;font-size:13px;color:#fff">Find a sitter now</div>
<div class="btn" style="left:556px;top:952px;width:88px;height:26px">Subscribe Now</div>

<!-- How it works -->
<svg class="abs" style="left:0;top:1000px" width="1200" height="560" viewBox="0 0 1200 560" aria-hidden="true">
  <path d="M0 60 C200 0 380 70 600 45 S980 10 1200 50 V470 C1000 440 820 520 600 505 S200 470 0 520 Z" fill="#f7b6c8"/>
  <path d="M0 500 C200 470 400 540 650 520 S1000 480 1200 500 V540 C1000 520 800 560 600 548 S200 530 0 545 Z" fill="#fbd3de"/>
</svg>
<h2 class="abs center" style="top:1100px;font-size:28px;font-weight:700;color:var(--navy)">How it Works</h2>
<svg class="abs" style="left:300px;top:1252px" width="600" height="2" aria-hidden="true"><line x1="0" y1="1" x2="600" y2="1" stroke="#fff" stroke-dasharray="4 4"/></svg>

<div class="step-circle" style="left:193px"><svg width="80" height="70" viewBox="0 0 80 70" fill="none" stroke="#2a2d6d" stroke-width="3"><rect x="6" y="24" width="68" height="40" rx="4"/><path d="M6 34h68M6 54h68M14 44l10 8 10-8 10 8 10-8 10 8"/><path d="M22 22 34 4M58 22 46 4"/></svg></div>
<div class="step-circle" style="left:404px"><svg width="90" height="60" viewBox="0 0 90 60" fill="none" stroke="#2a2d6d" stroke-width="3"><circle cx="18" cy="40" r="14"/><circle cx="72" cy="40" r="14"/><path d="M18 40 34 16h28l10 24M34 16l14 24 14-24M30 10h10M56 10h10"/></svg></div>
<div class="step-circle" style="left:618px"><svg width="70" height="70" viewBox="0 0 70 70" fill="none" stroke="#2a2d6d" stroke-width="3"><path d="M60 8 30 38l-8-8L52 2zM26 34 10 50M18 44l-12 4 4 12 8-4zM40 28l8 8"/></svg></div>
<div class="step-circle" style="left:830px"><svg width="84" height="56" viewBox="0 0 84 56" fill="none" stroke="#2a2d6d" stroke-width="3"><path d="M20 6h44a18 18 0 0 1 0 44H20A18 18 0 0 1 20 6z"/><path d="M22 20v16M14 28h16"/><circle cx="58" cy="22" r="3"/><circle cx="66" cy="32" r="3"/></svg></div>

<div class="step-title" style="left:174px">Lorem Ipsum is Simply</div>
<div class="step-title" style="left:385px">Lorem Ipsum is Simply</div>
<div class="step-title" style="left:599px">Lorem Ipsum is Simply</div>
<div class="step-title" style="left:811px">Lorem Ipsum is Simply</div>
<div class="step-text" style="left:174px">Lorem Ipsum is simply dummy<br>text of the printing.</div>
<div class="step-text" style="left:385px">Lorem Ipsum is simply dummy<br>text of the printing.</div>
<div class="step-text" style="left:599px">Lorem Ipsum is simply dummy<br>text of the printing.</div>
<div class="step-text" style="left:811px">Lorem Ipsum is simply dummy<br>text of the printing.</div>
<div class="btn" style="left:554px;top:1447px;width:92px;height:27px">Click View</div>

<!-- Testimonials -->
<div class="abs center eyebrow" style="top:1588px">Testimonials</div>
<h2 class="abs center heading-pink" style="top:1608px">What Client Say</h2>
<p class="abs para" style="left:440px;top:1652px;width:320px;text-align:center;font-size:13px;line-height:19px">Lorem Ipsum is simply dummy text of the printing and typesetting industry.</p>

<div class="quote" style="left:248px">“Lorem Ipsum is simply dummy text of the printing and typesetting industry. Lorem Ipsum is simply dummy text of the printing and typesetting industry.”</div>
<div class="quote" style="left:613px">“Lorem Ipsum is simply dummy text of the printing and typesetting industry. Lorem Ipsum is simply dummy text of the printing and typesetting industry.”</div>
<div class="avatar" style="left:286px" role="img" aria-label="Client portrait"></div>
<div class="who" style="left:338px">Lorem Ipsum<small>Lorem Ipsum is simply</small></div>
<div class="avatar" style="left:651px" role="img" aria-label="Client portrait"></div>
<div class="who" style="left:703px">Lorem Ipsum<small>Lorem Ipsum is simply</small></div>
<div class="btn" style="left:543px;top:1942px;width:114px;height:26px">View All Testimonials</div>

<!-- Children demographic -->
<svg class="abs" style="left:0;top:1990px" width="1200" height="580" viewBox="0 0 1200 580" aria-hidden="true">
  <path d="M0 40 C200 0 420 60 650 30 S1000 0 1200 30 V520 C1000 560 800 500 600 530 S200 560 0 510 Z" fill="#2a2d6d"/>
  <path d="M0 40 C250 70 500 20 760 45 S1050 70 1200 30 V90 C950 110 700 60 450 90 S150 100 0 80 Z" fill="#22255e"/>
  <path d="M0 460 C250 500 500 440 760 470 S1050 500 1200 470 V520 C1000 560 800 500 600 530 S200 560 0 510 Z" fill="#22255e"/>
</svg>
<h2 class="abs center" style="top:2108px;font-size:26px;font-weight:700;color:var(--pink)">Children Demographic</h2>
<div class="abs demo-photo" role="img" aria-label="Mother sitting with her toddler on the floor"></div>
<p class="abs demo-text">Lorem Ipsum is simply dummy text of the printing and typesetting industry. Lorem Ipsum has been the industry's standard dummy text ever since the 1500s, when an unknown printer took a galley of type and scrambled it to make a type specimen book.</p>
<div class="bullet" style="top:2324px"><i></i>Lorem Ipsum is simply dummy text of the printing.</div>
<div class="bullet" style="top:2358px"><i></i>Lorem Ipsum is simply dummy text of the printing.</div>
<div class="bullet" style="top:2392px"><i></i>Lorem Ipsum is simply dummy text of the printing.</div>
<div class="bullet" style="top:2426px"><i></i>Lorem Ipsum is simply dummy text of the printing.</div>

<!-- Blog -->
<div class="abs center eyebrow" style="top:2628px;font-size:14px">News &amp; Articles</div>
<h2 class="abs center heading-pink" style="top:2646px">From the Blog</h2>

<div class="ghost" style="left:180px">Lorem</div>
<div class="ghost" style="left:476px">Lorem</div>
<div class="ghost" style="left:772px">Lorem</div>
<div class="post-img" style="left:173px;background:linear-gradient(135deg,#3a2a2e,#a27064 60%,#5a3e3c)" role="img" aria-label="Mother and daughter hugging"></div>
<div class="post-img" style="left:469px;background:linear-gradient(135deg,#f1e4a4,#d8b66a 50%,#e8c7b8)" role="img" aria-label="Family playing outdoors"></div>
<div class="post-img" style="left:765px;background:linear-gradient(135deg,#e9d6c8,#c79c86 55%,#7f5f56)" role="img" aria-label="Smiling mother with child"></div>

<div class="post-title" style="left:181px">Lorem</div>
<div class="post-title" style="left:477px">Lorem</div>
<div class="post-title" style="left:773px">Lorem</div>
<div class="post-meta" style="left:181px">by Lorem Ipsum • Sep 17, 2018</div>
<div class="post-meta" style="left:477px">by Lorem Ipsum • Sep 17, 2018</div>
<div class="post-meta" style="left:773px">by Lorem Ipsum • Sep 17, 2018</div>
<p class="post-text" style="left:181px">Lorem Ipsum has been the industry's standard dummy text ever since the 1500s, when an unknown printer took a galley of type and scrambled it to make a type specimen book.</p>
<p class="post-text" style="left:477px">Lorem Ipsum has been the industry's standard dummy text ever since the 1500s, when an unknown printer took a galley of type and scrambled it to make a type specimen book.</p>
<p class="post-text" style="left:773px">Lorem Ipsum has been the industry's standard dummy text ever since the 1500s, when an unknown printer took a galley of type and scrambled it to make a type specimen book.</p>
<div class="btn" style="left:181px;top:3022px;width:86px;height:26px">Read More</div>
<div class="btn" style="left:477px;top:3022px;width:86px;height:26px">Read More</div>
<div class="btn" style="left:773px;top:3022px;width:86px;height:26px">Read More</div>

<!-- CTA -->
<svg class="abs" style="left:0;top:3070px" width="1200" height="214" viewBox="0 0 1200 214" aria-hidden="true">
  <path d="M0 30 C250 0 500 50 760 25 S1050 10 1200 30 V214 H0 Z" fill="#fbd3de"/>
  <path d="M0 60 C250 30 500 80 760 55 S1050 40 1200 60 V214 H0 Z" fill="#f7b6c8"/>
</svg>
<div class="abs center" style="top:3156px;font-size:17px;font-weight:700;color:var(--navy)">Need a Date Night?</div>
<div class="abs center" style="top:3180px;font-size:24px;font-weight:700;color:var(--navy)">Find a Sitter Now!</div>
<div class="btn" style="left:556px;top:3228px;width:88px;height:26px">Subscribe Now</div>

<!-- Footer -->
<footer class="abs footer"></footer>
<div class="f-col" style="left:244px">
  <div class="f-icon" style="background:var(--pink);border-radius:6px"><svg width="20" height="24" viewBox="0 0 20 24"><path d="M5 8a5 5 0 1 1 7 4.6c-1.2.6-2 1.4-2 2.9V17" stroke="#2a2d6d" stroke-width="3" fill="none"/><circle cx="10" cy="21.5" r="1.8" fill="#2a2d6d"/></svg></div>
  <h4>About Us</h4>
  <p>Lorem Ipsum is simply dummy text<br>of the printing and typesetting<br>industry.</p>
</div>
<div class="f-col" style="left:490px">
  <div class="f-icon"><svg width="40" height="40" viewBox="0 0 40 40" fill="none" stroke="#f7b6c8" stroke-width="3"><circle cx="20" cy="20" r="17"/><path d="M20 10v11l7 4"/></svg></div>
  <h4>Open Hours</h4>
  <p>Mon-Fri: 9 AM - 6 PM<br>Saturday: 9 AM - 4 PM<br>Emergency Available</p>
</div>
<div class="f-col" style="left:737px">
  <div class="f-icon"><svg width="38" height="38" viewBox="0 0 38 38" fill="none" stroke="#f7b6c8" stroke-width="3"><rect x="3" y="3" width="32" height="32" rx="2"/><circle cx="19" cy="15" r="5"/><path d="M9 31c1-6 5-9 10-9s9 3 10 9"/></svg></div>
  <h4>Contacts</h4>
  <p>48 Maple Lane, Brookfield 12345<br>Phone: 0 (555) 014-2270<br>Email: hello@huggasitter.com</p>
</div>
<div class="abs f-rule"></div>
<div class="abs f-logo">Hugga Sitter</div>
<div class="abs f-social"><span></span><span></span><span></span><span class="on"></span><span></span></div>
<div class="abs f-copy">© 2018 Hugga Sitter. All rights reserved.</div>

</body>
</html>
```